Vortapallo Rindelmo needs your help to create a new identity design

We are a basketball team based in Crescentino, Italy.
The official club colors are royal blue and white.
Basically we need a new letterhead and envelope design but not necessary a new logo, but if you want to suggest us a new one we are glad to evaluate it.
If you need any other info please contact us.

Target Market(s)

athletes, their families, other clubs, public institutions, companies

Industry/Entity Type

Club

Other font styles liked:
• the font of our logo or something very similar

Colors
0592cd
ffffff

Requirements
Must have
• our logo, attached to this request; address and other club info such as email address, phone number, facebook page, VAT lot and tax code and obviously our official club colors royal blue and white
Nice to have
• a clear, simple and quite minimal design. A watermark
Should not have
• any other graphic or images such as hoops, ball or court

```html
<!DOCTYPE html>
<html lang="en">
<head>
<meta charset="utf-8">
<title>Vortapallo Rindelmo Letterhead</title>
<link href="https://fonts.googleapis.com/css2?family=Open+Sans:wght@400;600;700&family=Saira+Condensed:ital,wght@1,800&display=swap" rel="stylesheet">
<style>
  :root {
    --backdrop: #e9eef5;
    --paper: #ffffff;
    --navy: #0b3a78;
    --royal: #0592cd;
    --accent-red: #e0401c;
    --rule-grey: #b3b3b3;
    --ink: #3a3a3a;
    --muted: #6d6d6d;
    --watermark: #eef2f7;
  }
  html, body {
    margin: 0;
    width: 1200px;
    height: 784px;
    overflow: hidden;
    background: var(--backdrop);
    font-family: "Open Sans", Arial, sans-serif;
  }
  .letterhead {
    position: absolute;
    left: 338px;
    top: 20px;
    width: 524px;
    height: 742px;
    background: linear-gradient(160deg, var(--paper) 55%, #eaf3fc 100%);
    box-shadow: 0 6px 22px rgba(20, 50, 100, .18);
    overflow: hidden;
  }
  .club-title {
    position: absolute;
    left: 26px;
    top: 26px;
    margin: 0;
    font-family: "Saira Condensed", "Arial Narrow", sans-serif;
    font-style: italic;
    font-weight: 800;
    font-size: 17px;
    letter-spacing: .3px;
    color: var(--navy);
    text-transform: uppercase;
  }
  .club-title .highlight { color: var(--royal); }
  .title-bar {
    position: absolute;
    left: 0;
    top: 50px;
    width: 280px;
    height: 10px;
  }
  .club-mark {
    position: absolute;
    right: 36px;
    top: 36px;
    display: flex;
    align-items: center;
    gap: 6px;
    font-weight: 700;
    font-size: 11px;
    color: var(--navy);
  }
  .club-mark .dot {
    width: 30px;
    height: 30px;
    border-radius: 50%;
    background: var(--royal);
  }
  .address-rule {
    position: absolute;
    left: 300px;
    right: 0;
    top: 82px;
    height: 4px;
    background: var(--rule-grey);
  }
  .header-address {
    position: absolute;
    right: 14px;
    top: 90px;
    margin: 0;
    font-size: 8.5px;
    font-weight: 700;
    color: var(--accent-red);
  }
  .watermark {
    position: absolute;
    left: 150px;
    top: 300px;
    width: 260px;
    height: 260px;
    border-radius: 50%;
    background: var(--watermark);
  }
  .letter-body {
    position: absolute;
    left: 118px;
    top: 118px;
    width: 330px;
    color: var(--ink);
    font-size: 8.6px;
    line-height: 1.55;
  }
  .salutation {
    margin: 0 0 12px;
    font-size: 12px;
    color: #555;
  }
  .letter-body p { margin: 0 0 12px; }
  .signature {
    position: absolute;
    left: 28px;
    top: 318px;
    width: 70px;
    height: 36px;
    background: #ececec;
    border-radius: 4px;
  }
  .footer-rule {
    position: absolute;
    left: 0;
    bottom: 0;
    width: 524px;
    height: 48px;
  }
  .footer-contacts {
    position: absolute;
    left: 14px;
    bottom: 28px;
    margin: 0;
    padding: 0;
    list-style: none;
    display: flex;
    gap: 10px;
    font-size: 7px;
    color: var(--muted);
    white-space: nowrap;
  }
  .footer-contacts li { display: flex; align-items: center; gap: 3px; }
  .footer-contacts .icon {
    width: 7px;
    height: 7px;
    border-radius: 50%;
    background: var(--navy);
  }
  .tax-code {
    position: absolute;
    right: 14px;
    bottom: 7px;
    margin: 0;
    font-size: 9px;
    font-weight: 600;
    color: #fff;
  }
</style>
</head>
<body>
<main class="letterhead">
  <h1 class="club-title">Vortapallo <span class="highlight">Rindelmo</span> Basketball</h1>
  <svg class="title-bar" viewBox="0 0 280 10" aria-hidden="true">
    <polygon points="0,0 274,0 280,10 0,10" fill="var(--navy)"/>
    <polygon points="0,0 200,0 204,4 0,4" fill="var(--royal)"/>
  </svg>

  <div class="club-mark"><span class="dot"></span>Vortapallo Rindelmo</div>
  <div class="address-rule"></div>
  <p class="header-address">Suite 4, 12 Via Lontana, Rindelmo Italy 0000</p>

  <div class="watermark" aria-hidden="true"></div>

  <article class="letter-body">
    <p class="salutation">Dear Mr. Solicitor,</p>
    <p>Lorem ipsum dolor sit amet, consectetur adipiscing elit. Vestibulum nec nunc sollicitudin, dictum ligula vitae, accumsan felis. Donec at quam felis. Pellentesque feugiat condimentum adipiscing. Maecenas sit amet neque ligula. Suspendisse ut libero in justo ullamcorper porttitor et vel orci. In consequat nibh in lacinia facilisis. Interdum et malesuada fames ac ante ipsum primis in faucibus. Cras adipiscing turpis lacus, eu faucibus nibh laoreet vel. Etiam pellentesque massa eu sodales interdum, mi nisi sagittis sem, sit amet feugiat turpis erat ac arcu. Proin at tincidunt nulla, sed feugiat massa. Maecenas suscipit purus nec orci rutrum, non auctor eros vulputate. Ut nec erat mollis, placerat risus venenatis, pharetra quam. Mauris hendrerit interdum ante, nec molestie ipsum faucibus eu.</p>
    <p>Nulla nec risus non quam mollis volutpat. Suspendisse sit amet dignissim purus. Sed fringilla ipsum eu ullamcorper posuere. In odio odio, tempor eu dictum a, pulvinar eu eros. Sed suscipit id risus a rhoncus. Mauris mollis dictum libero, vel lacinia sapien ullamcorper quis. Ut nec erat mollis, placerat risus venenatis, pharetra quam. Mauris hendrerit interdum ante, nec molestie ipsum faucibus eu. Etiam ut tristique sapien quis blandit ullamcorper, diam diam mollis urna, sed tempor diam nulla ut odio. Cras sollicitudin semper convallis. Sed suscipit id risus a rhoncus.</p>
  </article>
  <div class="signature" role="img" aria-label="Handwritten signature of the club president"></div>

  <svg class="footer-rule" viewBox="0 0 524 48" aria-hidden="true">
    <rect x="0" y="40" width="524" height="3" fill="var(--navy)"/>
    <rect x="0" y="44" width="524" height="4" fill="var(--royal)"/>
    <polygon points="400,22 524,22 524,48 386,48" fill="var(--navy)"/>
    <polygon points="0,36 120,36 124,40 0,40" fill="var(--rule-grey)"/>
  </svg>
  <ul class="footer-contacts">
    <li><span class="icon"></span>Suite 4, 12 Via Lontana, Rindelmo Italy 0000</li>
    <li><span class="icon"></span>(00) 0000 0000</li>
    <li><span class="icon"></span>example@example.com</li>
    <li><span class="icon"></span>@vortapallo</li>
    <li><span class="icon"></span>Vat</li>
  </ul>
  <p class="tax-code">TAX Code : 0000000000</p>
</main>
</body>
</html>
```